Thornbury Lettings Managment Ltd website

Need a website To inform people/clients of the services we provide. 5 pages total with a local feel. Bristol, UK. I have logo artwork already is like the look based on
incorporate the artwork attached for theme, feel and colours fonts info etc

To best describe the business have a brief look at www.fernwickhomes.example.co.uk which is a local firm offering the same services. This is for your ref only and not to be copied.

Target Market(s)

Property Investors/Landlords

Coding

Coded - Design and coding required

Number of Pages Required

5+ page

Colors
0392cd
f68d4d

Requirements
Must have
• local feel. Possibly using some local architecture or historic landmarks etc. This is fexible.
• most also be mobile device compatible
Nice to have
• the membership logos - files attached: KTB, DWF, GMV and safehold-example.co.uk

```html
<!DOCTYPE html>
<html lang="en">
<head>
<meta charset="utf-8">
<title>Thornbury Lettings Managment Ltd</title>
<link href="https://fonts.googleapis.com/css2?family=Open+Sans:wght@300;400;600;700&display=swap" rel="stylesheet">
<style>
:root{
  --teal:#2b6e85;
  --teal-light:#4a93ae;
  --teal-dark:#17475a;
  --ink:#2d2d2d;
  --text:#444;
  --white:#fff;
  --field:#fff;
  --black:#111;
  --grey-bg:#e9edf0;
}
*{box-sizing:border-box;margin:0;padding:0}
html,body{width:1200px;height:2719px;overflow:hidden;background:var(--white)}
body{font-family:"Open Sans",Arial,sans-serif;color:var(--text)}
.page{position:relative;width:1200px;height:2719px;overflow:hidden}
.abs{position:absolute}

/* header */
.site-header{left:0;top:0;width:1200px;height:165px;background:var(--white)}
.brand{left:40px;top:52px;display:flex;align-items:center;gap:14px}
.brand-square{width:48px;height:48px;background:var(--teal)}
.brand-name{font-weight:700;font-size:24px;color:var(--teal);line-height:1.15;width:250px}
.main-nav{right:30px;top:70px;display:flex;gap:10px;align-items:center}
.main-nav a{font-size:15px;font-weight:600;color:var(--ink);text-decoration:none;padding:7px 11px;border-radius:3px}
.main-nav a.active{background:var(--teal);color:var(--white)}

/* hero */
.hero{left:0;top:165px;width:1200px;height:500px;background:linear-gradient(180deg,#c9974f 0%,#7b6047 25%,#4d4a4a 55%,#2f3338 100%)}
.hero-title{left:0;width:1200px;top:330px;text-align:center;color:var(--white);font-weight:300;font-size:36px}
.hero-rule{left:300px;width:600px;top:385px;height:1px;background:rgba(255,255,255,.8)}
.hero-sub{left:0;width:1200px;top:397px;text-align:center;color:var(--white);font-weight:700;font-size:17px}

/* about */
.about{left:0;top:665px;width:1200px;height:340px;background:linear-gradient(180deg,var(--teal-light),var(--teal-dark))}
.about h2{position:absolute;left:0;width:1200px;top:32px;text-align:center;color:var(--white);font-weight:600;font-size:29px}
.about p{position:absolute;left:58px;top:90px;width:600px;color:var(--white);font-size:14.5px;line-height:1.6}
.video{position:absolute;left:743px;top:90px;width:400px;height:208px;border:6px solid var(--white);border-radius:3px;background:linear-gradient(180deg,#a9b8c4,#d9d3c5 55%,#8d8a83);box-shadow:0 4px 10px rgba(0,0,0,.35)}
.video svg{position:absolute;left:160px;top:66px}

/* feature rows */
.feature-img{top:0;height:400px}
.row{left:0;width:1200px;height:400px;overflow:hidden}
.row-landlords{top:1005px}
.row-agencies{top:1405px}
.row-tenants{top:1805px;height:400px}
.img-left{left:0;width:645px;clip-path:polygon(0 0,608px 0,645px 50%,608px 100%,0 100%)}
.img-right{left:545px;width:655px;clip-path:polygon(40px 0,100% 0,100% 100%,40px 100%,0 50%)}
.img-keys{background:linear-gradient(120deg,#8a8f96,#cfcfd2 45%,#6e7a94 100%)}
.img-house{background:linear-gradient(110deg,#8e9195,#5a5e63 50%,#2d3034)}
.img-couple{background:linear-gradient(120deg,#d9dde0,#f2f2f0 40%,#8a97b0 70%,#c7a884)}
.tag{width:175px;height:120px;background:var(--teal);color:var(--white);display:flex;flex-direction:column;align-items:center;justify-content:flex-end;padding-bottom:18px;gap:14px;font-weight:700;font-size:15px}
.feature-text{width:480px}
.feature-text h3{font-size:21px;font-weight:700;color:var(--ink);line-height:1.35;margin-bottom:18px}
.feature-text p{font-size:15px;line-height:1.55;color:var(--text);margin-bottom:20px}
.btn{display:block;width:308px;height:38px;line-height:38px;background:var(--teal);color:var(--white);text-align:center;font-weight:600;font-size:15.5px;border-radius:2px;text-decoration:none;box-shadow:0 3px 4px rgba(0,0,0,.25)}

/* footer */
.contact{left:0;top:2205px;width:1200px;height:350px;background:linear-gradient(180deg,var(--teal-light),var(--teal-dark))}
.foot-brand{left:78px;top:40px;display:flex;align-items:center;gap:14px}
.foot-brand .brand-square{background:var(--white)}
.foot-brand .brand-name{color:var(--white)}
.foot-line{left:78px;display:flex;align-items:flex-start;gap:12px;color:var(--white);font-weight:600;font-size:15.5px;line-height:1.45}
.social{left:110px;top:300px;display:flex;gap:8px}
.social span{width:16px;height:16px;border-radius:50%;background:var(--white)}
.field{background:var(--field);color:#666;font-size:13px;padding:8px 12px;border-radius:2px}
.send{background:var(--black);color:var(--white);font-weight:600;font-size:14px;text-align:center;line-height:37px;border:1px solid #888}

/* members */
.members{left:0;top:2555px;width:1200px;height:117px;background:var(--white)}
.members-label{left:190px;top:48px;font-weight:700;font-size:17px;color:var(--ink)}
.badge{top:30px;height:58px;border-radius:3px}
.copyright{left:0;top:2672px;width:1200px;height:47px;background:var(--teal);color:var(--white);text-align:center;line-height:47px;font-size:11.5px;font-weight:600}
</style>
</head>
<body>
<div class="page">

  <header class="site-header abs">
    <div class="brand abs">
      <span class="brand-square"></span>
      <span class="brand-name">Thornbury Lettings Managment Ltd</span>
    </div>
    <nav class="main-nav abs">
      <a href="#" class="active">HOME</a>
      <a href="#">ABOUT US</a>
      <a href="#">LANDLORDS</a>
      <a href="#">AGENCIES</a>
      <a href="#">TENANTS</a>
      <a href="#">CONTACT</a>
    </nav>
  </header>

  <section class="hero abs" role="img" aria-label="Aerial photo of Bristol rooftops at sunset"></section>
  <h1 class="hero-title abs">Thornbury Lettings Managment Ltd</h1>
  <div class="hero-rule abs"></div>
  <p class="hero-sub abs">THE IDEAL SOLUTION FOR LANDLORDS, TENANTS &amp; AGENCIES IN BRISTOL</p>

  <section class="about abs">
    <h2>About Us</h2>
    <p>Lorem ipsum dolor sit amet, consectetuer adipiscing elit, sed diam nonummy nibh euismod tincidunt ut laoreet dolore magna aliquam erat volutpat. Ut wisi enim ad minim veniam, quis nostrud exerci tation ullamcorper suscipit lobortis nisl ut aliquip ex ea commodo consequat. Duis autem vel eum iriure dolor in hendrerit in vulputate velit esse molestie consequat, vel illum dolore eu feugiat nulla facilisis at vero eros et accumsan et iusto odio dignissim qui blandit praesent luptatum zzril delenit augue duis dolore te feugait nulla facilisi.</p>
    <div class="video" role="img" aria-label="Video still of a curved Georgian terrace street">
      <svg width="68" height="68" viewBox="0 0 68 68"><circle cx="34" cy="34" r="32" fill="rgba(0,0,0,.55)"/><polygon points="27,20 50,34 27,48" fill="#fff"/></svg>
    </div>
  </section>

  <section class="row row-landlords abs">
    <div class="feature-img img-left img-keys abs" role="img" aria-label="Photo of a hand holding out house keys"></div>
    <div class="tag abs" style="left:0;top:143px">
      <svg width="70" height="24" viewBox="0 0 70 24"><circle cx="56" cy="12" r="10" fill="none" stroke="#fff" stroke-width="4"/><rect x="4" y="10" width="42" height="4" fill="#fff"/><rect x="8" y="14" width="4" height="7" fill="#fff"/><rect x="16" y="14" width="4" height="5" fill="#fff"/></svg>
      FOR LANDLORDS
    </div>
    <div class="feature-text abs" style="left:695px;top:30px">
      <h3>Guaranteed fixed rent – No bills, no voids, no maintenance, no hassle!</h3>
      <p>The process for landlords is simple. Instead of signing an agreement with a tenant, you sign a management contract with Thornbury Lettings Managment Ltd. You don't need to do anything else. This contract will last for a minimum of two years – but it could be several more if you wish to guarantee your rental payments for longer.</p>
      <p>We will then manage the property and tenants ourselves – you don't need to lift a finger.</p>
      <a href="#" class="btn" style="margin-left:73px">MORE ON FOR LANDLORDS</a>
    </div>
  </section>

  <section class="row row-agencies abs">
    <div class="feature-img img-right img-house abs" role="img" aria-label="Photo of a businessman holding a small model house in his palm"></div>
    <div class="tag abs" style="left:1025px;top:140px">
      <svg width="60" height="40" viewBox="0 0 60 40"><path d="M4 22 L16 10 L28 16 L40 10 L56 22 L40 34 L28 26 L20 34 Z" fill="none" stroke="#fff" stroke-width="3" stroke-linejoin="round"/></svg>
      FOR AGENCIES
    </div>
    <div class="feature-text abs" style="left:58px;top:30px;width:460px">
      <h3>5% Guaranteed commission, repeat business, no hassle!</h3>
      <p>Thornbury Lettings Managment Ltd is a unique property investment company, operating on multiple levels and is always looking for committed, integral and professional affiliates to help us deliver our service.</p>
      <p>Our aim is to provide quality accommodation to professional tenants with minimal hassle for their landlords.</p>
      <a href="#" class="btn" style="margin-left:70px">MORE ON FOR AGENCIES</a>
    </div>
  </section>

  <section class="row row-tenants abs">
    <div class="feature-img img-left img-couple abs" role="img" aria-label="Photo of a young couple sitting among moving boxes in a bright living room"></div>
    <div class="tag abs" style="left:0;top:148px">
      <svg width="48" height="44" viewBox="0 0 48 44"><path d="M6 22 L24 6 L42 22" fill="none" stroke="#fff" stroke-width="4" stroke-linejoin="round"/><rect x="14" y="20" width="20" height="18" fill="none" stroke="#fff" stroke-width="4"/></svg>
      FOR TENANTS
    </div>
    <div class="feature-text abs" style="left:695px;top:30px">
      <h3>Bills included, modern furniture, very fast broadband, like minded tenants</h3>
      <p>Companies or professional tenants who are interested in accommodation should use the contact button below.</p>
      <p>We are able to provide both short and long term tenancies, and may be able to find homes in your area if we do not currently have any availability.</p>
      <a href="#" class="btn" style="margin-left:68px">MORE ON FOR TENANTS</a>
    </div>
  </section>

  <footer class="contact abs">
    <div class="foot-brand abs">
      <span class="brand-square"></span>
      <span class="brand-name">Thornbury Lettings Managment Ltd</span>
    </div>
    <div class="foot-line abs" style="top:144px">
      <svg width="16" height="22" viewBox="0 0 16 22"><path d="M8 0 C3 0 0 4 0 8 C0 14 8 22 8 22 C8 22 16 14 16 8 C16 4 13 0 8 0 Z" fill="#fff"/><circle cx="8" cy="8" r="3" fill="#2b6e85"/></svg>
      <span>12 Hollis Row, Old Market<br>Bristol, BS2 9ZX</span>
    </div>
    <div class="foot-line abs" style="top:218px">
      <svg width="20" height="16" viewBox="0 0 20 16"><path d="M1 5 Q10 -2 19 5 L16 8 L13 5 L7 5 L4 8 Z" fill="#fff"/><rect x="4" y="8" width="12" height="8" rx="2" fill="#fff"/></svg>
      <span>0117 000 4417</span>
    </div>
    <div class="foot-line abs" style="top:260px">
      <svg width="18" height="14" viewBox="0 0 18 14"><rect x="0" y="0" width="18" height="14" fill="#fff"/><path d="M0 0 L9 8 L18 0" fill="none" stroke="#2b6e85" stroke-width="2"/></svg>
      <span>info@thornburylettings.example.co.uk</span>
    </div>
    <div class="social abs"><span></span><span></span></div>

    <div class="field abs" style="left:600px;top:118px;width:257px;height:37px">Name</div>
    <div class="field abs" style="left:866px;top:118px;width:257px;height:84px">Message</div>
    <div class="field abs" style="left:600px;top:165px;width:257px;height:37px">Email</div>
    <div class="field abs" style="left:600px;top:213px;width:257px;height:37px">Phone</div>
    <div class="send abs" style="left:866px;top:213px;width:109px;height:39px">SEND</div>
  </footer>

  <section class="members abs">
    <div class="members-label abs">MEMBERS OF</div>
    <div class="badge abs" style="left:366px;width:92px;background:#9b1c2a" aria-hidden="true"></div>
    <div class="badge abs" style="left:495px;width:223px;background:#9b86b8" aria-hidden="true"></div>
    <div class="badge abs" style="left:737px;width:46px;background:#2f8a9e" aria-hidden="true"></div>
    <div class="badge abs" style="left:820px;top:48px;height:24px;width:190px;background:#3a9bb8" aria-hidden="true"></div>
  </section>

  <div class="copyright abs">COPYRIGHT © 2016 THORNBURY LETTINGS MANAGMENT LTD. ALL RIGHTS RESERVED.</div>

</div>
</body>
</html>
```